Veltarum

Standard Business Card design.
Sample two-sided design uploaded. White front, Black back.
Would like white shield to be on all black background side.
Willing to look at a couple creative designs, but nothing crazy.
Preference for a classic, confident, strong design.

```html
<!DOCTYPE html>
<html lang="en">
<head>
<meta charset="utf-8">
<title>Veltarum Business Card</title>
<link href="https://fonts.googleapis.com/css2?family=Orbitron:wght@600&family=Montserrat:wght@400;500&display=swap" rel="stylesheet">
<style>
  :root {
    --backdrop: #d4d5d7;
    --card-white: #ffffff;
    --card-black: #050505;
    --ink-dark: #111111;
    --ink-light: #ffffff;
    --texture-mid: #1c1c1c;
    --texture-deep: #000000;
  }
  * { margin: 0; padding: 0; box-sizing: border-box; }
  html, body {
    width: 900px;
    height: 1200px;
    overflow: hidden;
    background: var(--backdrop);
  }
  .card {
    position: absolute;
    left: 133px;
    width: 634px;
    height: 364px;
    overflow: hidden;
  }
  .card-front {
    top: 210px;
    background: var(--card-white);
    display: flex;
    align-items: center;
    justify-content: center;
    gap: 18px;
  }
  .brand-square {
    width: 40px;
    height: 40px;
    background: var(--ink-dark);
  }
  .brand-name {
    font-family: "Orbitron", sans-serif;
    font-weight: 600;
    font-size: 34px;
    letter-spacing: 3px;
    color: var(--ink-dark);
  }
  .card-back {
    top: 624px;
    background: var(--card-black);
  }
  .back-texture {
    position: absolute;
    inset: 0;
    background:
      radial-gradient(ellipse 70% 55% at 70% 35%, var(--texture-mid) 0%, transparent 70%),
      linear-gradient(160deg, var(--texture-deep) 0%, #141414 45%, var(--texture-deep) 100%);
  }
  .back-mark {
    position: absolute;
    left: 529px;
    top: 58px;
    width: 56px;
    height: 56px;
    border: 5px solid var(--ink-light);
  }
  .holder {
    position: absolute;
    left: 39px;
    top: 208px;
    color: var(--ink-light);
    font-family: "Montserrat", sans-serif;
  }
  .holder-name {
    font-family: "Orbitron", sans-serif;
    font-weight: 600;
    font-size: 19px;
    letter-spacing: 1.5px;
  }
  .holder-role {
    font-size: 14px;
    margin-top: 5px;
  }
  .contact-list {
    list-style: none;
    margin-top: 14px;
  }
  .contact-item {
    display: flex;
    align-items: center;
    gap: 10px;
    font-size: 14.5px;
    letter-spacing: 1px;
    height: 23px;
  }
  .contact-icon {
    width: 14px;
    height: 14px;
    fill: var(--ink-light);
    flex-shrink: 0;
  }
</style>
</head>
<body>
  <section class="card card-front">
    <span class="brand-square"></span>
    <span class="brand-name">VELTARUM</span>
  </section>

  <section class="card card-back">
    <div class="back-texture" role="img" aria-label="Dark abstract architectural photograph of curving woven black panels"></div>
    <span class="back-mark"></span>
    <div class="holder">
      <p class="holder-name">MARA DELLCOURT</p>
      <p class="holder-role">Founder</p>
      <ul class="contact-list">
        <li class="contact-item">
          <svg class="contact-icon" viewBox="0 0 24 24"><path d="M6.6 10.8a15.1 15.1 0 0 0 6.6 6.6l2.2-2.2c.3-.3.7-.4 1-.2 1.1.4 2.3.6 3.6.6.6 0 1 .4 1 1V20c0 .6-.4 1-1 1C10.6 21 3 13.4 3 4c0-.6.4-1 1-1h3.5c.6 0 1 .4 1 1 0 1.3.2 2.5.6 3.6.1.3 0 .7-.2 1z"/></svg>
          <span>555-201-7480</span>
        </li>
        <li class="contact-item">
          <svg class="contact-icon" viewBox="0 0 24 24"><path d="M2 5h20v14H2z M2 5l10 8 10-8" fill="none" stroke="#fff" stroke-width="2"/><path d="M2 6l10 8 10-8v13H2z"/></svg>
          <span>info@veltarum.com</span>
        </li>
        <li class="contact-item">
          <svg class="contact-icon" viewBox="0 0 24 24"><circle cx="12" cy="12" r="9" fill="none" stroke="#fff" stroke-width="2"/><path d="M3 12h18M12 3c3 3 3 15 0 18M12 3c-3 3-3 15 0 18" fill="none" stroke="#fff" stroke-width="1.6"/></svg>
          <span>www.veltarum.com</span>
        </li>
      </ul>
    </div>
  </section>
</body>
</html>
```